File Download Website

We are looking for a design for a file download website. Our objective is to allow users to upload/browse/download files. This means we need 3 different pages.
The upload page should allow users to upload a file, we are looking for creative designs, a file box with a browse button next to it is already out there so the design must bring something new.
The browse page should display a users files/folders.
The download page should allow the user to download a file.
We do not require any code, only design. The designer is given complete freedom over the design, you may go about it however you like. This is a test of creativity, whoever this project goes to will definitely be given more work in the near future.
Example of a well designed file download website: cloudvane.net
Target Market(s)
15-30 year old people
Industry/Entity Type
Work
Look and feel
Each slider illustrates characteristics of the customer's brand and the style your logo design should communicate.

```html
<!DOCTYPE html>
<html lang="en">
<head>
<meta charset="utf-8">
<title>File Download Website – Page Layouts</title>
<link rel="stylesheet" href="https://fonts.googleapis.com/css2?family=Questrial&family=Montserrat:wght@400;600&display=swap">
<style>
  :root {
    --page-bg: #f4f4f4;
    --ink-soft: #8a8a8a;
    --ink-label: #b4b4b4;
    --link-blue: #7fd4f7;
    --divider: #8c8c8c;
    --teal: #13e0c4;
    --white: #ffffff;
    --panel-dark: rgba(18, 28, 34, 0.78);
    --menu-light: rgba(236, 238, 240, 0.92);
    --f-blue: #2b9cf0;
    --f-green: #2fe07a;
    --f-orange: #ff6a3a;
    --f-red: #ff3d5f;
    --f-yellow: #f7e21c;
    --pill-blue: #1aa6f0;
    --pill-yellow: #f0c419;
    --pill-red: #f2484e;
  }
  * { box-sizing: border-box; margin: 0; padding: 0; }
  html, body { width: 1200px; height: 1200px; overflow: hidden; }
  body {
    background: var(--page-bg);
    font-family: "Questrial", "Montserrat", sans-serif;
    position: relative;
  }
  .intro { position: absolute; left: 96px; top: 62px; }
  .intro-line { font-size: 23px; color: var(--ink-soft); letter-spacing: 0.5px; }
  .intro-link {
    margin-top: 14px; font-size: 30px; color: var(--link-blue);
    letter-spacing: 0.6px; font-family: "Montserrat", sans-serif; font-weight: 600;
    white-space: nowrap;
  }
  .section-label {
    position: absolute; left: 0; width: 1200px; text-align: center;
    font-family: "Montserrat", sans-serif; font-weight: 600;
    font-size: 10px; color: var(--ink-label); letter-spacing: 0.4px;
  }
  .divider { position: absolute; left: 0; top: 734px; width: 1200px; height: 3px; background: var(--divider); }
  .row { position: absolute; left: 30px; width: 1140px; display: flex; justify-content: space-between; }
  .row-top { top: 360px; }
  .row-bottom { top: 840px; }
  .screen {
    position: relative; width: 360px; height: 225px; overflow: hidden;
    color: var(--white); font-family: "Montserrat", sans-serif;
  }
  .backdrop { position: absolute; inset: 0; }
  .bg-meadow { background: linear-gradient(170deg, #2f7fb8 0%, #2d9aa6 40%, #6cbc6e 70%, #d9cf2c 100%); }
  .bg-dusk { background: linear-gradient(180deg, #f7b9a5 0%, #f29b8e 35%, #caa08e 60%, #9b8fa0 100%); }
  .bg-bloom { background: linear-gradient(160deg, #3a82c4 0%, #4fa9b4 35%, #9bc64a 65%, #e8d21e 100%); }
  .bg-coast { background: linear-gradient(180deg, #dfe7ea 0%, #6f8f98 35%, #2a4a52 60%, #2f9a96 80%, #e6ecea 100%); }
  .bg-petal { background: linear-gradient(160deg, #7bbf8c 0%, #c7d36a 40%, #f08a7a 70%, #e24c8a 100%); }
  .circle-btn {
    position: absolute; width: 36px; height: 36px; border: 1px solid rgba(255,255,255,.8);
    border-radius: 50%; font-size: 6px; display: flex; align-items: center; justify-content: center;
  }
  /* profile */
  .profile-tile {
    position: absolute; left: 95px; top: 72px; width: 52px; height: 52px; border-radius: 12px;
    background: var(--teal); display: flex; flex-direction: column; justify-content: center;
    padding-left: 22px; font-size: 8px; line-height: 1.1; font-weight: 600;
  }
  .profile-tile span { font-weight: 400; opacity: .85; }
  .greeting { position: absolute; left: 150px; top: 128px; font-size: 7px; }
  .split { position: absolute; left: 210px; top: 20px; width: 1px; height: 190px; background: rgba(255,255,255,.35); }
  .view-files { position: absolute; left: 232px; top: 104px; font-size: 7px; }
  .folder-ghost { position: absolute; left: 240px; top: 118px; width: 46px; height: 34px; border-radius: 3px; background: rgba(255,255,255,.55); }
  /* login */
  .brand-name {
    position: absolute; left: 0; width: 360px; top: 90px; text-align: center;
    font-family: "Montserrat", sans-serif; font-weight: 600; font-size: 16px;
    color: var(--white); letter-spacing: 0.5px;
  }
  .field {
    position: absolute; left: 148px; width: 64px; height: 7px; border: 1px solid rgba(255,255,255,.8);
    border-radius: 4px; font-size: 4px; padding-left: 4px; line-height: 5px;
  }
  .create-link { position: absolute; left: 152px; top: 146px; font-size: 4.5px; }
  /* info */
  .info-menu {
    position: absolute; left: 82px; top: 48px; width: 52px; height: 126px; background: rgba(230,230,230,.9);
    color: #777; font-size: 4.5px; padding: 12px 4px; line-height: 2.2; white-space: nowrap;
  }
  .info-menu .lower { margin-top: 8px; }
  .info-page {
    position: absolute; left: 134px; top: 40px; width: 108px; height: 140px; background: var(--white);
    color: #666; font-size: 3.5px; padding: 10px; line-height: 1.6;
  }
  .info-page h4 { font-size: 4.5px; color: #333; margin-bottom: 3px; }
  .info-page .arrow { position: absolute; left: 3px; top: 12px; color: var(--pill-blue); font-size: 6px; }
  .txt-line { height: 1px; background: #bbb; margin: 3px 0; }
  /* browse */
  .drive {
    position: absolute; left: 94px; top: 50px; width: 168px; height: 118px; background: var(--panel-dark); padding: 8px;
  }
  .search { height: 6px; border: 1px solid rgba(255,255,255,.7); border-radius: 3px; width: 70px; font-size: 3.5px; padding-left: 3px; line-height: 4px; }
  .folder-grid { display: grid; grid-template-columns: repeat(3, 30px); gap: 10px 12px; margin-top: 8px; }
  .folder-item { font-size: 3.5px; line-height: 1.2; }
  .folder {
    position: relative; width: 16px; height: 12px; border-radius: 2px; margin-top: 3px; margin-bottom: 2px; background: var(--c);
  }
  .folder::before { content: ""; position: absolute; left: 0; top: -2px; width: 7px; height: 3px; background: var(--c); border-radius: 1px 1px 0 0; }
  .view-toggle { position: absolute; right: 18px; top: 8px; width: 10px; height: 6px; background: rgba(255,255,255,.8); }
  .plus-btn { position: absolute; right: 6px; top: 6px; width: 8px; height: 8px; border: 1px solid #fff; border-radius: 50%; font-size: 6px; line-height: 6px; text-align: center; }
  .action-menu {
    position: absolute; width: 42px; background: var(--menu-light); color: #555; font-size: 3.8px; padding: 4px; line-height: 2.3;
    white-space: nowrap;
  }
  .action-menu .act::before { content: ""; display: inline-block; width: 4px; height: 4px; border: 0.6px solid #555; border-radius: 50%; margin-right: 2px; vertical-align: middle; }
  .action-menu .settings { text-align: right; font-weight: 600; }
  .pager { position: absolute; left: 0; width: 360px; text-align: center; font-size: 4px; }
  .dots { display: flex; gap: 3px; justify-content: center; margin-top: 4px; }
  .dots i { width: 3px; height: 3px; border-radius: 50%; background: #fff; opacity: .9; }
  .dots i.on { background: var(--pill-blue); }
  .dots i.dim { background: #333; }
  /* explorer */
  .explorer { position: absolute; left: 88px; top: 50px; width: 194px; height: 140px; display: flex; }
  .sidebar { width: 58px; background: rgba(12,16,20,.92); padding: 4px; font-size: 3.5px; }
  .sidebar .search { width: 50px; margin-bottom: 6px; }
  .side-item { display: flex; gap: 3px; align-items: center; margin-bottom: 7px; }
  .side-item .folder { width: 14px; height: 11px; margin: 2px 0 0; }
  .contents { flex: 1; background: var(--white); color: #444; font-size: 3.5px; padding: 4px 6px; position: relative; }
  .crumb { font-weight: 600; margin-bottom: 6px; }
  .contents .arrow { position: absolute; left: 2px; top: 18px; color: var(--pill-blue); font-size: 6px; }
  .cols { display: flex; gap: 4px; margin-left: 6px; }
  .col { width: 56px; }
  .col + .col { border-left: 1px solid #ddd; padding-left: 3px; height: 104px; width: 52px; }
  .pill {
    height: 5px; border: 0.8px solid var(--pc); border-radius: 3px; margin-bottom: 3px; font-size: 3px;
    line-height: 3.6px; padding: 0 3px; display: flex; justify-content: space-between; white-space: nowrap;
  }
  .pill.fill { background: var(--pc); color: #fff; }
</style>
</head>
<body>

<header class="intro">
  <p class="intro-line">please download high resolution example:</p>
  <p class="intro-link">https://www.sharebin.net/f/q7x2lmnpa04/preview-sheet.jpg</p>
</header>

<p class="section-label" style="top:290px">Home, log In and Information pages</p>

<section class="row row-top">
  <article class="screen profile-page">
    <div class="backdrop bg-meadow" role="img" aria-label="Soft blurred blue, green and yellow photo backdrop"></div>
    <div class="profile-tile">edit<span>profile</span></div>
    <p class="greeting">Hello, <strong>Avery</strong></p>
    <div class="split"></div>
    <p class="view-files">view my files</p>
    <div class="folder-ghost"></div>
    <div class="circle-btn" style="left:104px;top:176px">learn more</div>
  </article>

  <article class="screen login-page">
    <div class="backdrop bg-dusk" role="img" aria-label="Blurred pebble beach photo at pink sunset"></div>
    <p class="brand-name">cloudvane</p>
    <div class="field" style="top:122px">username</div>
    <div class="field" style="top:133px">password</div>
    <p class="create-link">⊕ create new account</p>
    <div class="circle-btn" style="left:163px;top:168px">learn more</div>
  </article>

  <article class="screen info-page-screen">
    <div class="backdrop bg-bloom" role="img" aria-label="Photo of a yellow poppy against a blue and green blur"></div>
    <nav class="info-menu">
      storage &amp; product<br>sharing<br>access<br>collaboration<br>desktop &amp; mobile
      <div class="lower">registers<br>FAQ<br>contact</div>
    </nav>
    <div class="info-page">
      <span class="arrow">›</span>
      <h4>Section 1</h4>
      <div class="txt-line"></div><div class="txt-line"></div><div class="txt-line"></div><div class="txt-line"></div>
      <div class="txt-line"></div><div class="txt-line"></div><div class="txt-line"></div><div class="txt-line"></div>
      <h4 style="margin-top:8px">Section 2</h4>
      <div class="txt-line"></div><div class="txt-line"></div><div class="txt-line"></div><div class="txt-line"></div>
      <div class="txt-line"></div><div class="txt-line"></div><div class="txt-line"></div>
    </div>
    <div class="circle-btn" style="left:262px;top:166px">learn more</div>
  </article>
</section>

<div class="divider"></div>
<p class="section-label" style="top:775px">Upload and Browse Pages</p>

<section class="row row-bottom">
  <article class="screen browse-page">
    <div class="backdrop bg-coast" role="img" aria-label="Blurred coastal rocks and sea photo"></div>
    <div class="drive">
      <div class="search">Search</div>
      <div class="view-toggle"></div><div class="plus-btn">+</div>
      <div class="folder-grid">
        <div class="folder-item"><div class="folder" style="--c:var(--f-blue)"></div>Final Artwork</div>
        <div class="folder-item"><div class="folder" style="--c:var(--f-green)"></div>Drafts Version 2</div>
        <div class="folder-item"><div class="folder" style="--c:var(--f-orange)"></div>Example Images</div>
        <div class="folder-item"><div class="folder" style="--c:var(--f-red)"></div>Text Edited</div>
        <div class="folder-item"><div class="folder" style="--c:var(--f-yellow)"></div>Reference Docs</div>
        <div class="folder-item"><div class="folder" style="--c:var(--f-green)"></div>Drafts V1</div>
      </div>
    </div>
    <div class="action-menu" style="left:236px;top:118px">
      <div class="act">Upload file</div><div class="act">Create folder</div><div class="act">New folder</div><div class="act">Download</div>
      <div class="settings">Settings</div>
    </div>
    <div class="pager" style="top:180px">Design Workshop
      <div class="dots"><i class="dim"></i><i class="dim"></i><i class="dim"></i><i class="on"></i><i></i><i></i><i></i><i></i><i></i><i></i></div>
    </div>
  </article>

  <article class="screen explorer-page">
    <div class="backdrop bg-coast" role="img" aria-label="Blurred coastal rocks and sea photo"></div>
    <div class="explorer">
      <aside class="sidebar">
        <div class="search">Search</div>
        <div class="side-item"><div class="folder" style="--c:var(--f-blue)"></div>Final Artwork</div>
        <div class="side-item"><div class="folder" style="--c:var(--f-green)"></div>Drafts Version 2</div>
        <div class="side-item"><div class="folder" style="--c:var(--f-orange)"></div>Example Images</div>
        <div class="side-item"><div class="folder" style="--c:var(--f-red)"></div>Text Edited</div>
        <div class="side-item"><div class="folder" style="--c:var(--f-yellow)"></div>Reference Docs</div>
      </aside>
      <div class="contents">
        <p class="crumb">Design Workshop › Final Artwork</p>
        <span class="arrow">›</span>
        <div class="cols">
          <div class="col">
            <div class="pill fill" style="--pc:var(--pill-blue)"><span>Cover art</span><span>folder</span></div>
            <div class="pill" style="--pc:var(--pill-blue)"><span>Poster draft</span><span>folder</span></div>
            <div class="pill" style="--pc:var(--pill-blue)"><span>Stock images</span><span>folder</span></div>
            <div class="pill" style="--pc:var(--pill-yellow)"><span>Header.png</span><span>image</span></div>
            <div class="pill" style="--pc:var(--pill-yellow)"><span>Badge.png</span><span>image</span></div>
            <div class="pill" style="--pc:var(--pill-yellow)"><span>Notes.txt</span><span>text</span></div>
            <div class="pill" style="--pc:var(--pill-yellow)"><span>Brief.txt</span><span>text</span></div>
          </div>
          <div class="col">
            <div class="pill" style="--pc:var(--pill-blue)"><span>Sub folder 01</span></div>
            <div class="pill" style="--pc:var(--pill-blue)"><span>Sub folder 02</span></div>
            <div class="pill fill" style="--pc:var(--pill-red)"><span>Invoice.pdf</span></div>
            <div class="pill" style="--pc:var(--pill-red)"><span>Report.pdf</span><span>pdf</span></div>
          </div>
        </div>
      </div>
    </div>
    <div class="action-menu" style="left:272px;top:40px">
      <div class="act">Upload file</div><div class="act">Create folder</div><div class="act">New folder</div><div class="act">Download</div>
      <div class="settings">Settings</div>
    </div>
    <div class="pager" style="top:200px">Design Workshop
      <div class="dots"><i></i><i></i><i></i><i></i><i class="on"></i><i></i><i></i><i></i><i></i><i></i></div>
    </div>
  </article>

  <article class="screen browse-page">
    <div class="backdrop bg-petal" role="img" aria-label="Soft focus photo of pink and yellow flower petals"></div>
    <div class="drive">
      <div class="search">Search</div>
      <div class="view-toggle"></div><div class="plus-btn">+</div>
      <div class="folder-grid">
        <div class="folder-item"><div class="folder" style="--c:var(--f-blue)"></div>Final Artwork</div>
        <div class="folder-item"><div class="folder" style="--c:var(--f-green)"></div>Drafts Version 2</div>
        <div class="folder-item"><div class="folder" style="--c:var(--f-orange)"></div>Example Images</div>
        <div class="folder-item"><div class="folder" style="--c:var(--f-red)"></div>Text Edited</div>
        <div class="folder-item"><div class="folder" style="--c:var(--f-yellow)"></div>Reference Docs</div>
        <div class="folder-item"><div class="folder" style="--c:var(--f-green)"></div>Drafts V1</div>
      </div>
    </div>
    <div class="action-menu" style="left:236px;top:118px">
      <div class="act">Upload file</div><div class="act">Create folder</div><div class="act">New folder</div><div class="act">Download</div>
      <div class="settings">Settings</div>
    </div>
    <div class="pager" style="top:180px">
      <div class="dots"><i class="dim"></i><i class="dim"></i><i class="dim"></i><i class="on"></i><i></i><i></i><i></i><i></i><i></i><i></i></div>
    </div>
  </article>
</section>

</body>
</html>
```